Redesign and move to Wordpress for quarvendo.com

Our website needs a redesign and at the same time we are moving it to Wordpress. Please help us with a new digital professional look and feel.

We are an Australian Software Engineering company specialising in advanced software development using in A.I., PLatform Engineering, Integration and Cloud. See the current quarvendo.com for more information about us.

```html
<!DOCTYPE html>
<html lang="en">
<head>
<meta charset="utf-8">
<title>quarvendo — Reliable. Smart. Custom. Software.</title>
<link href="https://fonts.googleapis.com/css2?family=Plus+Jakarta+Sans:wght@600;700;800&family=Space+Grotesk:wght@400;500;700&display=swap" rel="stylesheet">
<style>
  :root {
    --ink: #0b0b0b;
    --black: #000;
    --white: #fff;
    --teal: #52c4bc;
    --blue: #1c6fbf;
    --page: #fbfbfb;
    --section: #f7f7f7;
    --card: #f2f2f2;
    --rule: #e2e2e2;
    --muted: #3b3b3b;
  }
  * { box-sizing: border-box; margin: 0; padding: 0; }
  html, body { width: 921px; height: 1200px; overflow: hidden; background: var(--page); }
  body { position: relative; font-family: "Space Grotesk", sans-serif; color: var(--ink); }

  .site { position: absolute; left: 60px; top: 56px; width: 800px; height: 1144px; background: var(--white); border-left: 1px solid var(--rule); border-right: 1px solid var(--rule); box-shadow: 0 0 24px rgba(0,0,0,0.04); }

  .masthead { position: absolute; left: 0; top: 0; width: 800px; height: 71px; background: var(--black); }
  .brand { position: absolute; left: 13px; top: 12px; display: flex; align-items: center; gap: 10px; }
  .brand-mark { width: 32px; height: 32px; border: 3px solid var(--white); }
  .brand-name { color: var(--white); font-size: 23px; font-weight: 400; letter-spacing: 1.5px; line-height: 1; }
  .brand-tagline { position: absolute; left: 59px; top: 46px; color: var(--white); font-size: 10px; }

  .btn { position: absolute; display: flex; align-items: center; justify-content: center; gap: 8px; background: var(--teal); color: var(--white); font-family: "Plus Jakarta Sans", sans-serif; font-weight: 700; font-size: 14px; box-shadow: 0 -3px 6px rgba(82,196,188,0.35); }
  .btn-header { left: 630px; top: 14px; width: 158px; height: 43px; }

  .hero-title { position: absolute; left: 15px; top: 149px; font-family: "Plus Jakarta Sans", sans-serif; font-weight: 800; font-size: 45px; line-height: 51px; letter-spacing: -1px; white-space: nowrap; }
  .hero-title .accent { color: var(--blue); }
  .hero-lede { position: absolute; left: 15px; top: 257px; width: 372px; font-size: 17px; line-height: 22.5px; }
  .btn-hero { left: 15px; top: 349px; width: 182px; height: 43px; }

  .hero-visual { position: absolute; left: 532px; top: 150px; width: 214px; height: 214px; background: linear-gradient(135deg, #1c6fbf 0%, #2a7ec0 45%, #52c4bc 100%); opacity: 0.9; }

  .rule { position: absolute; left: 0; width: 800px; border-top: 2px dotted var(--rule); }

  .clients { position: absolute; left: 0; top: 468px; width: 800px; height: 94px; }
  .client { position: absolute; top: 36px; display: flex; align-items: center; gap: 7px; font-weight: 700; font-size: 20px; color: #3a3a3a; transform: translateX(-50%); white-space: nowrap; }
  .client-dot { width: 12px; height: 12px; border-radius: 50%; background: #3a3a3a; }

  .expertise { position: absolute; left: 0; top: 562px; width: 800px; height: 582px; background: var(--section); background-image: radial-gradient(#ececec 1px, transparent 1px); background-size: 12px 12px; }
  .expertise-title { position: absolute; left: 0; top: 58px; width: 800px; text-align: center; font-family: "Plus Jakarta Sans", sans-serif; font-weight: 700; font-size: 27.5px; line-height: 34px; letter-spacing: -0.3px; }

  .card { position: absolute; background: var(--card); padding: 7px 13px; }
  .card-icon { width: 46px; height: 46px; background: #f7f7f7; display: flex; align-items: center; justify-content: center; margin-bottom: 13px; }
  .card-icon svg { width: 26px; height: 26px; stroke: var(--teal); fill: none; stroke-width: 1.6; stroke-linecap: round; stroke-linejoin: round; }
  .card h3 { font-weight: 700; font-size: 12px; line-height: 14px; margin-bottom: 9px; }
  .card p { font-size: 11.3px; line-height: 14px; color: var(--muted); }
  .card-link { position: absolute; right: 13px; bottom: 6px; width: 100px; height: 26px; border: 1px solid #555; background: var(--white); display: flex; align-items: center; justify-content: center; gap: 6px; font-size: 11px; color: var(--ink); }
</style>
</head>
<body>
<div class="site">
  <header class="masthead">
    <div class="brand">
      <span class="brand-mark"></span>
      <span class="brand-name">quarvendo</span>
    </div>
    <span class="brand-tagline">Tomorrow, delivered today.</span>
    <a class="btn btn-header">Talk To Our CTO</a>
  </header>

  <section class="hero">
    <h1 class="hero-title">Reliable. Smart.<br>Custom. S<span class="accent">o</span>ftware.</h1>
    <p class="hero-lede">Delivering cutting-edge digital solutions for health, finance, and enterprise industries.</p>
    <a class="btn btn-hero">Talk To Our CTO
      <svg width="12" height="12" viewBox="0 0 12 12" fill="none" stroke="#fff" stroke-width="1.6"><path d="M2 10 10 2M4 2h6v6"/></svg>
    </a>
    <div class="hero-visual" role="img" aria-label="3D illustration of four blue and teal frames forming a window grid"></div>
  </section>

  <div class="rule" style="top:467px"></div>

  <section class="clients" aria-label="Clients">
    <span class="client" style="left:127px">Norvex</span>
    <span class="client" style="left:336px"><span class="client-dot"></span>Calloway Super</span>
    <span class="client" style="left:525px">Bramblecore</span>
    <span class="client" style="left:675px">Tarrant Freight</span>
  </section>

  <div class="rule" style="top:561px"></div>

  <section class="expertise">
    <h2 class="expertise-title">Our Expertise at a Glance</h2>

    <article class="card" style="left:131px; top:118px; width:168px; height:174px;">
      <div class="card-icon"><svg viewBox="0 0 26 26"><circle cx="10" cy="10" r="7"/><circle cx="16" cy="16" r="7"/></svg></div>
      <h3>Enterprise Integration</h3>
      <p>Automate internal and external workflows seamlessly.</p>
    </article>

    <article class="card" style="left:316px; top:118px; width:169px; height:174px;">
      <div class="card-icon"><svg viewBox="0 0 26 26"><rect x="10.5" y="2" width="5" height="5"/><rect x="4" y="18" width="5" height="5"/><rect x="17" y="18" width="5" height="5"/><path d="M13 7v5M2 12h22M6.5 12v6M19.5 12v6"/></svg></div>
      <h3>Microservices Architecture</h3>
      <p>Build agile, independent, and scalable modules.</p>
    </article>

    <article class="card" style="left:502px; top:118px; width:168px; height:174px;">
      <div class="card-icon"><svg viewBox="0 0 26 26"><ellipse cx="13" cy="6" rx="9" ry="3.5"/><path d="M4 6v14c0 2 4 3.5 9 3.5s9-1.5 9-3.5V6M4 11c0 2 4 3.5 9 3.5s9-1.5 9-3.5M4 15.5c0 2 4 3.5 9 3.5s9-1.5 9-3.5"/></svg></div>
      <h3>Real-Time Data Processing</h3>
      <p>React instantly to changes with actionable insights.</p>
    </article>

    <article class="card" style="left:131px; top:309px; width:354px; height:160px;">
      <div class="card-icon"><svg viewBox="0 0 26 26"><circle cx="13" cy="11" r="4"/><path d="M6 24c0-4 3-7 7-7s7 3 7 7"/><circle cx="6" cy="6" r="2.6"/><circle cx="20" cy="6" r="2.6"/><path d="M1.5 15c0-3 2-5 4.5-5M24.5 15c0-3-2-5-4.5-5"/></svg></div>
      <h3>Custom Solutions for SMBs</h3>
      <p>Affordable and powerful systems tailored for small to<br>medium businesses.</p>
      <a class="card-link">Learn More
        <svg width="10" height="10" viewBox="0 0 12 12" fill="none" stroke="#222" stroke-width="1.4"><path d="M2 10 10 2M4 2h6v6"/></svg>
      </a>
    </article>

    <article class="card" style="left:502px; top:309px; width:168px; height:160px;">
      <div class="card-icon"><svg viewBox="0 0 26 26"><rect x="1.5" y="3" width="23" height="20"/><path d="M6 9l4 4-4 4M12 17h6"/></svg></div>
      <h3>Legacy System Enablement</h3>
      <p>Modernize outdated systems with cutting-edge tech.</p>
    </article>
  </section>

  <div class="rule" style="top:1090px"></div>
</div>
</body>
</html>
```